BrovaLT BIZ Card, email signature & Stationary

Professional business cards, email signatures and ms word letterhead

Target Market(s)

business owners

Industry/Entity Type

cloud hosting

Contact Information for Business Card

name title office phone number , direct line, fax email address web site

Font styles to use
Other font styles liked:
• something that compliments font in logo

```html
<!DOCTYPE html>
<html lang="en">
<head>
<meta charset="utf-8">
<title>BrovaLT Business Card</title>
<link rel="stylesheet" href="https://fonts.googleapis.com/css2?family=Montserrat:wght@300;400;500;600;700;800&display=swap">
<style>
  :root {
    --brand-red: #e0141e;
    --ink: #111111;
    --paper: #ffffff;
    --paper-shade: #ededed;
    --card-dark: #141414;
    --card-dark-top: #2a2a2a;
    --stage: #2b2828;
    --muted: #3a3a3a;
  }
  * { box-sizing: border-box; margin: 0; padding: 0; }
  html, body {
    width: 1200px; height: 901px; overflow: hidden;
    background: var(--stage);
    font-family: "Montserrat", sans-serif;
  }
  .sheet {
    position: relative; width: 1200px; height: 901px;
    display: flex; align-items: center; justify-content: center; gap: 56px;
  }
  .card {
    position: relative; width: 520px; height: 298px;
    border-radius: 18px;
    box-shadow: 0 5px 0 var(--brand-red), 0 20px 40px rgba(0,0,0,.5);
    overflow: hidden;
  }
  /* Front */
  .card-front {
    background: linear-gradient(160deg, var(--paper) 55%, var(--paper-shade));
    color: var(--ink);
  }
  .wordmark {
    position: absolute; left: 34px; top: 150px;
    font-weight: 300; font-size: 54px; letter-spacing: -1px;
    color: var(--brand-red); line-height: 1;
  }
  .divider {
    position: absolute; left: 262px; top: 50px; width: 3px; height: 200px;
    background: var(--ink);
  }
  .divider::before {
    content: ""; position: absolute; left: 0; top: 0; width: 3px; height: 34px;
    background: var(--brand-red);
  }
  .details {
    position: absolute; left: 288px; top: 52px; width: 220px;
  }
  .person-name { font-size: 19px; font-weight: 400; line-height: 1.05; }
  .person-name strong { font-weight: 800; }
  .person-title { font-size: 11px; font-weight: 400; color: var(--muted); margin-top: 2px; }
  .rule { width: 14px; height: 2px; background: var(--ink); margin: 12px 0 8px; }
  .address { font-size: 10.5px; font-weight: 600; line-height: 1.35; }
  .contact-list { list-style: none; }
  .contact-list li {
    display: flex; align-items: center; gap: 8px;
    font-size: 11px; font-weight: 600; line-height: 1; margin-bottom: 6px;
  }
  .contact-list svg { width: 13px; height: 13px; flex: none; }
  /* Back */
  .card-back {
    background: radial-gradient(ellipse at 30% 15%, var(--card-dark-top), var(--card-dark) 65%);
    display: flex; flex-direction: column; align-items: center; justify-content: center;
  }
  .card-back .wordmark {
    position: static; font-size: 62px;
  }
  .web-pill {
    margin-top: 26px; display: flex; align-items: center; gap: 10px;
    padding: 5px 16px 5px 6px;
    border: 1.5px solid #555; border-radius: 20px;
    color: #ffffff; font-size: 12px; font-weight: 500; letter-spacing: 5px;
  }
  .web-pill svg { width: 16px; height: 16px; }
</style>
</head>
<body>
<main class="sheet">
  <section class="card card-front" aria-label="Business card front">
    <div class="wordmark">BrovaLT</div>
    <div class="divider"></div>
    <div class="details">
      <p class="person-name">Daniel <strong>Korvath</strong></p>
      <p class="person-title">Project Manager</p>
      <div class="rule"></div>
      <p class="address">No.14, Harbor Lane<br>Dalton 400, Wexford, USA</p>
      <div class="rule"></div>
      <ul class="contact-list">
        <li><svg viewBox="0 0 16 16"><path d="M4 2l3 3-1.5 2a8 8 0 0 0 3.5 3.5L11 9l3 3-2 2C7 14 2 9 2 4z" fill="var(--brand-red)"/></svg>0198 765 432</li>
        <li><svg viewBox="0 0 16 16"><rect x="4" y="1.5" width="8" height="13" rx="1.5" fill="none" stroke="var(--brand-red)" stroke-width="1.6"/><circle cx="8" cy="12" r="0.9" fill="var(--brand-red)"/></svg>0198 765 433</li>
        <li><svg viewBox="0 0 16 16"><rect x="4" y="1.5" width="8" height="4" fill="none" stroke="var(--brand-red)" stroke-width="1.4"/><rect x="1.5" y="6" width="13" height="6" rx="1" fill="var(--brand-red)"/><rect x="4" y="10" width="8" height="4.5" fill="#fff" stroke="var(--brand-red)" stroke-width="1.4"/></svg>0198 765 434</li>
        <li><svg viewBox="0 0 16 16"><rect x="1.5" y="3.5" width="13" height="9" fill="none" stroke="var(--brand-red)" stroke-width="1.6"/><path d="M1.5 3.5L8 9l6.5-5.5" fill="none" stroke="var(--brand-red)" stroke-width="1.6"/></svg>hello@BrovaLT.com</li>
        <li><svg viewBox="0 0 16 16"><circle cx="8" cy="8" r="6.5" fill="var(--brand-red)"/><path d="M1.5 8h13M8 1.5c-3 3-3 10 0 13M8 1.5c3 3 3 10 0 13" fill="none" stroke="#fff" stroke-width="1"/></svg>www.BrovaLT.com</li>
      </ul>
    </div>
  </section>

  <section class="card card-back" aria-label="Business card back">
    <div class="wordmark">BrovaLT</div>
    <div class="web-pill">
      <svg viewBox="0 0 16 16"><circle cx="8" cy="8" r="6.5" fill="var(--brand-red)"/><path d="M1.5 8h13M8 1.5c-3 3-3 10 0 13M8 1.5c3 3 3 10 0 13" fill="none" stroke="#141414" stroke-width="1"/></svg>
      www.BrovaLT.com
    </div>
  </section>
</main>
</body>
</html>
```